Beautiful e-comm site for 'roadside farmers stand' online!

Need a logo design and basic e-comm website (super super simple) for new business called Brindlecove. Brindlecove is an online farmers stand where local artisans can sell 'brindlecove' goods directly from their makers!

Looking for something simple, whimsicle and clean! (Ideally with a light grey or perrywinkle and some color mixed in - word 'Brindlecove' in black - can work the pear shape in somewhere but not required!)

Target Market(s)

Hobby shoppers and 'quilo' goers who want a focus on edible things and care about ingredients!

Industry/Entity Type

E-Commerce

Number of Pages Required

2 page

Font styles to use
Decorative
Script

Colors
f3f1f8
ec1f27
cadf82

Requirements
Must have
• - Basic logo
• - Homepage
• - Product Detail Page
• - Be in a responsive, woocommerce or shopify, wordpress theme (will purchase theme after design is approved)
Nice to have
• - Matching check out & cart pages
• - 'About Us' page
• - SEO plugin
Should not have
• A cluttered look/feel.

```html
<!DOCTYPE html>
<html lang="en">
<head>
<meta charset="utf-8">
<title>Brindlecove — Mix Vegetable Pickle</title>
<link href="https://fonts.googleapis.com/css2?family=Montserrat:wght@300;400;500;600;700&display=swap" rel="stylesheet">
<style>
  :root {
    --red: #c11d24;
    --red-bright: #ec1f27;
    --green: #cadf82;
    --ink: #111111;
    --body-text: #222222;
    --white: #ffffff;
    --grey-band: #e6e6e6;
    --grey-footer: #ebebeb;
    --rule: #dddddd;
    --header-sky: #b9d6e6;
  }
  * { box-sizing: border-box; margin: 0; padding: 0; }
  html, body { width: 1200px; height: 2486px; overflow: hidden; }
  body {
    position: relative;
    font-family: "Montserrat", Arial, sans-serif;
    color: var(--body-text);
    background: var(--white);
  }
  .abs { position: absolute; }

  /* Header */
  .site-header {
    position: absolute; left: 0; top: 0; width: 1200px; height: 90px;
    background: linear-gradient(90deg, #b6d3e4 0%, #c9e0ec 45%, #b3cfe2 100%);
  }
  .brand {
    position: absolute; left: 120px; top: 22px;
    font-size: 34px; font-weight: 700; color: var(--ink); letter-spacing: -0.5px;
  }
  .main-nav { position: absolute; top: 38px; left: 0; width: 1200px; }
  .main-nav a {
    position: absolute; font-size: 16px; font-weight: 500; color: var(--ink);
    text-decoration: none; letter-spacing: 0.3px;
  }
  .nav-marker {
    position: absolute; left: 493px; top: -9px; width: 18px; height: 18px;
    border-radius: 50%; background: var(--red-bright);
  }
  .cart-button {
    position: absolute; left: 1021px; top: 18px; width: 61px; height: 52px;
    background: var(--red); border-radius: 3px; color: var(--white);
    font-size: 11px; font-weight: 500; text-align: center;
  }
  .cart-button svg { position: absolute; left: 19px; top: 8px; }
  .cart-button .cart-label { position: absolute; left: 0; width: 61px; top: 32px; }
  .cart-count {
    position: absolute; left: 41px; top: 3px; width: 16px; height: 16px; border-radius: 50%;
    background: var(--green); color: var(--ink); font-size: 10px; font-weight: 600;
    line-height: 16px; text-align: center;
  }

  /* Hero */
  .hero {
    position: absolute; left: 0; top: 90px; width: 1200px; height: 304px;
    background: radial-gradient(circle at 10% 40%, #e9b13c 0 9%, transparent 10%),
                radial-gradient(circle at 75% 30%, #7fa83a 0 10%, transparent 11%),
                radial-gradient(circle at 55% 75%, #b8324a 0 8%, transparent 9%),
                linear-gradient(90deg, #d9a35c 0%, #c97a4a 30%, #d8b8a0 55%, #9fa84d 80%, #d98a6a 100%);
  }
  .hero::after { content: ""; position: absolute; inset: 0; background: rgba(90,40,20,0.25); }
  .hero-title {
    position: absolute; left: 0; top: 124px; width: 1200px; text-align: center; z-index: 1;
    color: var(--white); font-size: 33px; font-weight: 700; letter-spacing: 0.5px;
  }

  /* Section headings with rule ornaments */
  .ruled-heading { position: absolute; left: 0; width: 1200px; text-align: center; font-weight: 300; }
  .ruled-line { position: absolute; height: 1px; }
  .ruled-line::before, .ruled-line::after {
    content: ""; position: absolute; top: -3px; width: 5px; height: 5px;
    border: 1px solid currentColor; border-radius: 50%; background: var(--white);
  }
  .ruled-line.left::before { left: -6px; }
  .ruled-line.left::after { display: none; }
  .ruled-line.right::after { right: -6px; }
  .ruled-line.right::before { display: none; }

  /* Product detail */
  .product-title { top: 468px; font-size: 30px; color: var(--red); }
  .product-title-line { top: 491px; background: var(--red); color: var(--red); }
  .product-photo {
    position: absolute; left: 113px; top: 575px; width: 434px; height: 429px;
    background: radial-gradient(ellipse at 50% 50%, #e4a04a 0 18%, #b7a86a 30%, #8d8474 55%, #6e665b 100%);
  }
  .product-copy { position: absolute; left: 600px; top: 573px; width: 478px; font-size: 13.5px; line-height: 19px; color: var(--body-text); }
  .product-copy p + p { margin-top: 13px; }
  .rule { position: absolute; height: 1px; background: var(--rule); }
  .price { position: absolute; left: 606px; top: 852px; font-size: 42px; font-weight: 700; color: var(--red); }
  .qty {
    position: absolute; left: 751px; top: 857px; width: 139px; height: 48px;
    border: 1px solid #cfcfcf; background: var(--white);
  }
  .qty-value { position: absolute; left: 14px; top: 13px; font-size: 15px; }
  .qty-plus { position: absolute; right: -1px; top: -1px; width: 54px; height: 48px; background: var(--green); }
  .add-to-cart {
    position: absolute; left: 600px; top: 948px; width: 157px; height: 46px;
    border: 1px solid var(--red); border-radius: 3px; color: var(--red);
    font-size: 15px; font-weight: 600; letter-spacing: 1px; text-align: center; line-height: 44px;
  }

  /* Related products */
  .related { position: absolute; left: 0; top: 1097px; width: 1200px; height: 466px; background: var(--grey-band); }
  .related-title { top: 80px; font-size: 31px; color: var(--ink); }
  .product-card {
    position: absolute; top: 147px; width: 227px; height: 242px;
    background: var(--white); border: 1px solid var(--red); border-radius: 4px; overflow: hidden;
  }
  .card-photo { height: 136px; }
  .card-name { position: absolute; left: 0; top: 155px; width: 100%; text-align: center; font-size: 17px; font-weight: 500; color: var(--ink); }
  .card-price { position: absolute; left: 83px; top: 195px; width: 60px; height: 47px; }
  .card-price span {
    position: absolute; left: 0; top: 17px; width: 60px; text-align: center;
    color: var(--white); font-size: 16px; font-weight: 700;
  }

  /* Newsletter */
  .newsletter {
    position: absolute; left: 0; top: 1563px; width: 1200px; height: 444px;
    background: radial-gradient(circle at 20% 30%, #f3ddc8 0 12%, transparent 30%),
                radial-gradient(circle at 75% 25%, #f4c0b4 0 15%, transparent 35%),
                radial-gradient(circle at 85% 80%, #f2c8b8 0 10%, transparent 30%),
                linear-gradient(180deg, #fbf3ee 0%, #f7ece6 100%);
  }
  .newsletter-title { top: 127px; font-size: 31px; color: var(--ink); }
  .newsletter-line { top: 150px; background: var(--ink); color: var(--ink); }
  .newsletter-line::before, .newsletter-line::after { background: transparent; }
  .newsletter-text { position: absolute; left: 190px; top: 196px; width: 820px; text-align: center; font-size: 15.5px; line-height: 21px; color: var(--ink); }
  .email-field {
    position: absolute; left: 386px; top: 270px; width: 285px; height: 46px;
    border: 1px solid var(--red); background: var(--white);
    font-size: 15px; font-style: italic; color: #333; padding: 14px 10px;
  }
  .subscribe {
    position: absolute; left: 686px; top: 270px; width: 129px; height: 46px;
    background: var(--red); color: var(--white); font-size: 15px; font-weight: 700;
    text-align: center; line-height: 46px; letter-spacing: 0.5px;
  }

  /* Footer */
  .site-footer { position: absolute; left: 0; top: 2007px; width: 1200px; height: 479px; background: var(--grey-footer); }
  .footer-banner { position: absolute; left: 118px; top: 87px; }
  .footer-brand { position: absolute; left: 138px; top: 128px; font-size: 32px; font-weight: 700; color: var(--white); letter-spacing: -0.5px; }
  .footer-about { position: absolute; left: 138px; top: 195px; width: 340px; font-size: 13.5px; line-height: 17px; color: var(--white); }
  .social-tile { position: absolute; top: 281px; width: 29px; height: 29px; background: var(--white); }
  .footer-heading { position: absolute; top: 159px; font-size: 14px; font-weight: 600; color: var(--red); letter-spacing: 0.3px; }
  .footer-links { position: absolute; top: 184px; list-style: none; font-size: 14px; line-height: 25.5px; color: var(--ink); }
  .footer-links li::before { content: "• "; }
  .copyright { position: absolute; left: 566px; top: 300px; font-size: 14px; color: var(--ink); }
  .footer-policy { position: absolute; left: 983px; top: 300px; font-size: 14px; color: var(--ink); }
</style>
</head>
<body>

<header class="site-header">
  <div class="brand">Brindlecove</div>
  <nav class="main-nav">
    <span class="nav-marker"></span>
    <a style="left:481px">HOME</a>
    <a style="left:557px">PRODUCT</a>
    <a style="left:668px">STORES</a>
    <a style="left:761px">WHO WE ARE</a>
    <a style="left:900px">CONTACT</a>
  </nav>
  <div class="cart-button">
    <svg width="22" height="20" viewBox="0 0 22 20" fill="none" stroke="#fff" stroke-width="2">
      <path d="M1 2h4l3 11h11l2-8H7"/>
      <circle cx="9" cy="17" r="1.6" fill="#fff"/>
      <circle cx="17" cy="17" r="1.6" fill="#fff"/>
    </svg>
    <span class="cart-count">2</span>
    <span class="cart-label">CART</span>
  </div>
</header>

<section class="hero" role="img" aria-label="Close-up of colourful jelly sweets and sprinkles">
  <h1 class="hero-title">PICKLES</h1>
</section>

<main>
  <h2 class="ruled-heading product-title">Mix Vegetable Pickle</h2>
  <span class="ruled-line left product-title-line" style="left:279px;width:144px"></span>
  <span class="ruled-line right product-title-line" style="left:779px;width:138px"></span>

  <div class="product-photo" role="img" aria-label="Glass jar of mixed vegetable pickle on a checked cloth"></div>

  <div class="product-copy">
    <p>Fusce lectus eros, congue at urna non, rhoncus pulvinar nunc. Nulla cursus bibendum scelerisque. Ut vulputate rhoncus bibendum. Maecenas molestie pretium porta. Praesent sed quam eget velit consequat viverra ut ac urna. Nam aliquam nunc vitae sollicitudin mattis. Ut urna neque, dictum at tortor ut, dictum porta orci. In felis mauris, dictum a ligula a, egestas pharetra magna. Integer ornare ac libero nec tincidunt. Quisque eu pulvinar odio, eu feugiat diam.</p>
    <p>Curabitur id magna urna. Duis non interdum sem. Phasellus egestas libero vitae commodo consequat. Aliquam nec aliquet neque, sed tempus dui. Praesent fermentum erat sed orci maximus, at euismod dolor condimentum. Ut eleifend aliquet enim, ac tempor sem consectetur euismod.</p>
  </div>

  <span class="rule" style="left:600px;top:843px;width:478px"></span>
  <div class="price">$11</div>
  <div class="qty">
    <span class="qty-value">1</span>
    <span class="qty-plus">
      <svg width="54" height="48" viewBox="0 0 54 48"><path d="M27 16v16M19 24h16" stroke="#111" stroke-width="2.5"/></svg>
    </span>
  </div>
  <span class="rule" style="left:600px;top:915px;width:478px"></span>
  <div class="add-to-cart">ADD TO CART</div>
</main>

<section class="related">
  <h2 class="ruled-heading related-title">You May Also Be Interested In</h2>

  <article class="product-card" style="left:118px">
    <div class="card-photo" role="img" aria-label="Cherries and a jar of jam in a basket" style="background:linear-gradient(135deg,#7a9a5a,#a0242e 55%,#c23a44)"></div>
    <h3 class="card-name">Cherry Fruit Jams</h3>
    <div class="card-price"><svg width="60" height="47"><path d="M0 0L30 10L60 0V47H0Z" fill="#c11d24"/></svg><span>$10</span></div>
  </article>

  <article class="product-card" style="left:365px">
    <div class="card-photo" role="img" aria-label="Bowl of egg salad" style="background:radial-gradient(circle at 50% 55%,#d9964a 0 25%,#c9c08a 45%,#f2eee4 75%)"></div>
    <h3 class="card-name">Egg Salad</h3>
    <div class="card-price"><svg width="60" height="47"><path d="M0 0L30 10L60 0V47H0Z" fill="#c11d24"/></svg><span>$18</span></div>
  </article>

  <article class="product-card" style="left:611px">
    <div class="card-photo" role="img" aria-label="Stack of fresh cookies" style="background:linear-gradient(180deg,#23252a 0%,#5a4228 55%,#b27a3a 80%,#c8c2b8)"></div>
    <h3 class="card-name">Fresh Cookies</h3>
    <div class="card-price"><svg width="60" height="47"><path d="M0 0L30 10L60 0V47H0Z" fill="#c11d24"/></svg><span>$08</span></div>
  </article>

  <article class="product-card" style="left:857px">
    <div class="card-photo" role="img" aria-label="Plate of colourful jelly beans" style="background:radial-gradient(circle at 50% 50%,#e8a03a 0 15%,#6fb84a 30%,#d94a5a 45%,#e6e6e6 70%)"></div>
    <h3 class="card-name">Colourfull Jelly Beens</h3>
    <div class="card-price"><svg width="60" height="47"><path d="M0 0L30 10L60 0V47H0Z" fill="#c11d24"/></svg><span>$14</span></div>
  </article>
</section>

<section class="newsletter" role="img" aria-label="Faded background of jam jars and fruit">
  <h2 class="ruled-heading newsletter-title">Sign up for Special Offers and Stories</h2>
  <span class="ruled-line left newsletter-line" style="left:221px;width:77px"></span>
  <span class="ruled-line right newsletter-line" style="left:903px;width:75px"></span>
  <p class="newsletter-text">Suspendisse odio quam, mollis id semper non, finibus sit amet nulla. Vivamus malesuada est eu tristique sodales. Morbi a sem odio.</p>
  <div class="email-field">Enter your Email ID</div>
  <div class="subscribe">SUBSCRIBE</div>
</section>

<footer class="site-footer">
  <svg class="footer-banner" width="387" height="307" viewBox="0 0 387 307">
    <path d="M0 0H387V307L198 280L0 307Z" fill="#c11d24"/>
  </svg>
  <div class="footer-brand">Brindlecove</div>
  <p class="footer-about">Curabitur id magna urna. Duis non interdum sem. Phasellus egestas libero vitae commodo consequat. Aliquam nec aliquet neque, sed tempus dui.</p>
  <span class="social-tile" style="left:139px"></span>
  <span class="social-tile" style="left:177px"></span>
  <span class="social-tile" style="left:215px"></span>
  <span class="social-tile" style="left:253px"></span>

  <h4 class="footer-heading" style="left:567px">CUSTOMER SERVICE</h4>
  <ul class="footer-links" style="left:567px">
    <li>Contact Us</li>
    <li>Returns</li>
    <li>Site Map</li>
  </ul>

  <h4 class="footer-heading" style="left:860px">INFORMATION</h4>
  <ul class="footer-links" style="left:860px">
    <li>Delivery Information</li>
    <li>Privacy Policy</li>
    <li>Terms &amp; Conditions</li>
  </ul>

  <span class="rule" style="left:530px;top:272px;width:547px;background:#cccccc"></span>
  <p class="copyright">© 2018 Brindlecove. All Rights Reserved.</p>
  <p class="footer-policy">Privacy Policy</p>
</footer>

</body>
</html>
```